Lumoran signs for fridge and desk

I require 3 a4 designs very basic designs with single colour and easy to print. I have atached a style guide to see the fonts I used in my last three design. Please remember I'm printing in only one colour
PLease see the following link, of what I sell on quorbit. I will be selling this allong side these products.
https://www.quorbitshop.example/gp/item/K42H9XRDLM
Please see my competitors
https://www.quorbitshop.example/Planner-Magnetic-Calendar-Refrigerator-Container/dp/K7TQR2ZMWA/ref=sr_1_8?keywords=acrylic%2Bnote%2Bboard%2Brefrigerator%2Bdry%2Berase%2Bboard%2Bmagnetic%2Bclear&qid=1500000001&sr=8-8&th=1
and
https://www.quorbitshop.example/Magnetic-Acrylic-Calendar-Fridge-Refrigerator/dp/K9PWX4HNVE/ref=sr_1_4_sspa?keywords=acrylic+note+board+refrigerator+dry+erase+board+magnetic+clear&qid=1500000002&sr=8-4-spons&psc=1&spLa=UXhMbTNwZkRzWXZLcTJ3Rm5CaFRnSmRWZUx5UG1Sb1phSXVPY0F0TmJXa0dmWnNZeEhqUXJUbkxwVmRNZ0ViS2N5SXdBb0J1RnpQbVhoU2pOdFlxUmdDa1d2RHNMZUZuSHBaeEJtQ2tUZ1lqVnJRc0Vh
I'd like something more fun and different. But that can still be printed on Lumoran with one colour and be functional. A shopping list, a weekly planner(both that stick to a fridge) and a to do list that will sit on a desk or kitchen counter top.
PLease design
1st a4
Break into seven parts, with seven headings..... Monday to Sunday.... here customers will be able to write menus and upcoming events. I want this landcape
2nd a4
'Shopping List' is to be the heading
I want this landcape
3rd a4
'To Do List' is the only text I would like
I would like this portrat and lines marked and a check box on the left hand side
Remember I can only print on the acrylic with one colour. I want to be different from my competitors but I do want to be functional.
just a reminder. I can only print with one colour

```html
<!DOCTYPE html>
<html lang="en">
<head>
<meta charset="utf-8">
<title>Lumoran signs for fridge and desk</title>
<link href="https://fonts.googleapis.com/css2?family=Great+Vibes&family=Montserrat:ital,wght@1,400;1,600&family=Oswald:wght@400;500&display=swap" rel="stylesheet">
<style>
  :root {
    --backdrop: #6f6f6f;
    --board: #8b8b8b;
    --doodle-a: #a2a2a2;
    --doodle-b: #8f8f8f;
    --ink: #ffffff;
  }
  * { margin: 0; padding: 0; box-sizing: border-box; }
  html, body { width: 1200px; height: 950px; overflow: hidden; }
  body { background: var(--backdrop); position: relative; }

  .board {
    position: absolute;
    border-radius: 11px;
    overflow: hidden;
    background: linear-gradient(135deg, var(--doodle-a), var(--doodle-b));
  }
  .board--shopping { left: 72px; top: 32px; width: 558px; height: 389px; }
  .board--weekly   { left: 72px; top: 527px; width: 558px; height: 389px; }
  .board--todo     { left: 757px; top: 196px; width: 389px; height: 558px; }

  .board__doodles { position: absolute; inset: 0; }
  .board__art { position: absolute; inset: 0; width: 100%; height: 100%; }

  .frame { fill: var(--board); stroke: var(--ink); stroke-width: 1.6; }
  .box { fill: none; stroke: var(--ink); stroke-width: 1.3; }
  .rule { fill: none; stroke: var(--ink); stroke-width: 0.9; }
  .icon { fill: none; stroke: var(--ink); stroke-width: 1.8; stroke-linejoin: round; stroke-linecap: round; }

  .title { font-family: "Great Vibes", cursive; fill: var(--ink); font-size: 40px; }
  .label { font-family: "Montserrat", sans-serif; font-style: italic; font-weight: 600; font-size: 8.5px; fill: var(--ink); }
  .field-label { font-family: "Montserrat", sans-serif; font-style: italic; font-weight: 400; font-size: 9px; fill: var(--ink); }
  .notes-pill { fill: var(--ink); }
  .notes-pill-text { font-family: "Montserrat", sans-serif; font-style: italic; font-weight: 600; font-size: 8px; fill: var(--board); }
  .caps { font-family: "Oswald", sans-serif; font-weight: 500; font-size: 12.5px; fill: var(--ink); }
</style>
</head>
<body>

<!-- Shopping list board -->
<section class="board board--shopping">
  <div class="board__doodles" role="img" aria-label="Border of hand-drawn grocery doodles: vegetables, fruit, seafood and pantry items"></div>
  <svg class="board__art" viewBox="0 0 558 389" xmlns="http://www.w3.org/2000/svg">
    <defs>
      <path id="shop-rules" class="rule" d="M6 36h93m-93 19.8h93m-93 19.8h93m-93 19.8h93m-93 19.8h93m-93 19.8h93m-93 19.8h93m-93 19.8h93m-93 19.8h93m-93 19.8h93m-93 19.8h93"/>
    </defs>
    <path class="frame" d="M49 22H509A22 22 0 0 0 531 44V344A22 22 0 0 0 509 366H49A22 22 0 0 0 27 344V44A22 22 0 0 0 49 22Z"/>

    <g class="icon basket">
      <path d="M144 33h26l-3 13h-20z"/>
      <path d="M150 33l4-9m10 9l-4-9"/>
      <path d="M152 36v7m5-7v7m5-7v7"/>
    </g>
    <text class="title" x="190" y="64" textLength="178" lengthAdjust="spacingAndGlyphs">Shopping List</text>
    <g class="icon cart">
      <path d="M384 27h6l4 16h16l3-11h-21"/>
      <path d="M398 32v11m6-11v11"/>
      <circle cx="396" cy="48" r="2"/>
      <circle cx="408" cy="48" r="2"/>
    </g>

    <g class="column" transform="translate(52 87)">
      <rect class="box" width="105" height="254" rx="5"/>
      <path class="rule" d="M0 15h105"/>
      <text class="label" x="52.5" y="11" text-anchor="middle">Groceries</text>
      <use href="#shop-rules"/>
    </g>
    <g class="column" transform="translate(169 87)">
      <rect class="box" width="105" height="254" rx="5"/>
      <path class="rule" d="M0 15h105"/>
      <text class="label" x="52.5" y="11" text-anchor="middle">Online</text>
      <use href="#shop-rules"/>
    </g>
    <g class="column" transform="translate(285 87)">
      <rect class="box" width="105" height="254" rx="5"/>
      <path class="rule" d="M0 15h105"/>
      <text class="label" x="52.5" y="11" text-anchor="middle">Other</text>
      <use href="#shop-rules"/>
    </g>
    <g class="column" transform="translate(401 87)">
      <rect class="box" width="105" height="254" rx="5"/>
      <path class="rule" d="M0 15h105"/>
      <text class="label" x="52.5" y="11" text-anchor="middle">Notes:</text>
      <use href="#shop-rules"/>
    </g>
  </svg>
</section>

<!-- Weekly planner board -->
<section class="board board--weekly">
  <div class="board__doodles" role="img" aria-label="Border of hand-drawn leaves, flowers and cacti with a looped spiral trim along the top"></div>
  <svg class="board__art" viewBox="0 0 558 389" xmlns="http://www.w3.org/2000/svg">
    <defs>
      <path id="day-rules" class="rule" d="M6 34h92m-92 19.7h92m-92 19.7h92m-92 19.7h92"/>
    </defs>
    <path class="frame" d="M47 25H511A22 22 0 0 0 533 47V343A22 22 0 0 0 511 365H47A22 22 0 0 0 25 343V47A22 22 0 0 0 47 25Z"/>

    <text class="title" x="62" y="70" textLength="205" lengthAdjust="spacingAndGlyphs">Weekly Planner</text>
    <rect class="box" x="288" y="51" width="104" height="15" rx="6"/>
    <text class="field-label" x="294" y="62">Week Of :</text>
    <rect class="box" x="401" y="51" width="104" height="15" rx="6"/>
    <text class="field-label" x="407" y="62">Month :</text>

    <rect class="notes-pill" x="54" y="93" width="40" height="14" rx="7"/>
    <text class="notes-pill-text" x="74" y="103" text-anchor="middle">Notes:</text>
    <path class="rule" d="M54 126h104m-104 19.7h104m-104 19.7h104m-104 19.7h104m-104 19.7h104"/>

    <g class="day" transform="translate(169 92)">
      <rect class="box" width="104" height="114" rx="5"/>
      <path class="rule" d="M0 15h104"/>
      <text class="label" x="52" y="11" text-anchor="middle">Monday</text>
      <use href="#day-rules"/>
    </g>
    <g class="day" transform="translate(286 92)">
      <rect class="box" width="104" height="114" rx="5"/>
      <path class="rule" d="M0 15h104"/>
      <text class="label" x="52" y="11" text-anchor="middle">Tuesday</text>
      <use href="#day-rules"/>
    </g>
    <g class="day" transform="translate(401 92)">
      <rect class="box" width="104" height="114" rx="5"/>
      <path class="rule" d="M0 15h104"/>
      <text class="label" x="52" y="11" text-anchor="middle">Wednesday</text>
      <use href="#day-rules"/>
    </g>
    <g class="day" transform="translate(54 221)">
      <rect class="box" width="104" height="113" rx="5"/>
      <path class="rule" d="M0 15h104"/>
      <text class="label" x="52" y="11" text-anchor="middle">Thursday</text>
      <use href="#day-rules"/>
    </g>
    <g class="day" transform="translate(169 221)">
      <rect class="box" width="104" height="113" rx="5"/>
      <path class="rule" d="M0 15h104"/>
      <text class="label" x="52" y="11" text-anchor="middle">Friday</text>
      <use href="#day-rules"/>
    </g>
    <g class="day" transform="translate(286 221)">
      <rect class="box" width="104" height="113" rx="5"/>
      <path class="rule" d="M0 15h104"/>
      <text class="label" x="52" y="11" text-anchor="middle">Saturday</text>
      <use href="#day-rules"/>
    </g>
    <g class="day" transform="translate(401 221)">
      <rect class="box" width="104" height="113" rx="5"/>
      <path class="rule" d="M0 15h104"/>
      <text class="label" x="52" y="11" text-anchor="middle">Sunday</text>
      <use href="#day-rules"/>
    </g>
  </svg>
</section>

<!-- To do list board -->
<section class="board board--todo">
  <div class="board__doodles" role="img" aria-label="Border of hand-drawn everyday doodles: coffee cups, plants, music notes, travel and hobby items"></div>
  <svg class="board__art" viewBox="0 0 389 558" xmlns="http://www.w3.org/2000/svg">
    <defs>
      <g id="todo-row">
        <rect class="box" x="42" y="143" width="14" height="14"/>
        <path class="rule" d="M65 157H348"/>
      </g>
    </defs>
    <path class="frame" d="M46 28H343A22 22 0 0 0 365 50V508A22 22 0 0 0 343 530H46A22 22 0 0 0 24 508V50A22 22 0 0 0 46 28Z"/>

    <text class="title" x="125" y="72" textLength="140" lengthAdjust="spacingAndGlyphs">To Do List</text>

    <g class="weekdays">
      <text class="caps" x="98" y="100" text-anchor="middle">SUN</text>
      <text class="caps" x="132" y="100" text-anchor="middle">MON</text>
      <text class="caps" x="165" y="100" text-anchor="middle">TUE</text>
      <text class="caps" x="198" y="100" text-anchor="middle">WED</text>
      <text class="caps" x="231" y="100" text-anchor="middle">THU</text>
      <text class="caps" x="261" y="100" text-anchor="middle">FRI</text>
      <text class="caps" x="291" y="100" text-anchor="middle">SAT</text>
    </g>
    <text class="caps" x="130" y="122">DATE :</text>
    <path class="rule" d="M164 122H259"/>

    <g class="checklist">
      <use href="#todo-row"/>
      <use href="#todo-row" y="31.3"/>
      <use href="#todo-row" y="62.6"/>
      <use href="#todo-row" y="93.9"/>
      <use href="#todo-row" y="125.2"/>
      <use href="#todo-row" y="156.5"/>
      <use href="#todo-row" y="187.8"/>
      <use href="#todo-row" y="219.1"/>
      <use href="#todo-row" y="250.4"/>
      <use href="#todo-row" y="281.7"/>
    </g>

    <text class="caps" x="194" y="465" text-anchor="middle">NOTES:</text>
    <path class="rule" d="M42 493H348"/>
  </svg>
</section>

</body>
</html>
```